New Corporate Business Card - Velmorabelle

What we need:
We need a new corporate business card.
We want a new template that we can change by ourself.
We want business card modern and minimalist but that looks professional.
We will print it in 300 gr soft-touch.
Why not a white side with the logo and a red/grey side with the content?
Why not a grey side and a red side like our logo?
I am sure that you have better idea than ours that's the reason we come here.

Who we are:
We are a private label company in cosmetics based in Switzerland. We work in BtoB. We make skin care products for other brands.

Target Market(s)

B to B - Worldwide - any gender

Industry/Entity Type

Cosmetics

Contact Information for Business Card

Side 1:
Logo
Your Swiss Private Label Manufacturer or www.velmorabelle.ch

Side 2:
Name and surname (Example: Lucien Marchetaz)
Job Description (General Manager)
Telephone (+41 32 918 64 00)
Direct (+41 32 918 64 64)
Email (lucien.marchetaz@velmorabelle.ch)
Chemin des Prés-Fleuris 14, 2000 Neuchâtel, Switzerland
www.velmorabelle.ch

Font styles to use
Serif
Sans Serif

Requirements
Must have
• You can use 4 colors: white, red, grey and/or black .
Should not have
• Too much colors, too much things. We want it simple!

```html
<!DOCTYPE html>
<html lang="en">
<head>
<meta charset="utf-8">
<title>Velmorabelle – Business Card</title>
<link rel="stylesheet" href="https://fonts.googleapis.com/css2?family=Open+Sans:wght@300;400;600;700&display=swap">
<style>
  :root {
    --red: #e31e36;
    --grey: #9d9d9d;
    --grey-dark: #6f6f6f;
    --white: #ffffff;
    --ink: #1c1c1c;
    --backdrop: #2b2b2b;
  }
  * { box-sizing: border-box; margin: 0; padding: 0; }
  html, body { width: 1200px; height: 900px; overflow: hidden; }
  body {
    background: var(--backdrop);
    font-family: "Open Sans", sans-serif;
    position: relative;
  }
  .card {
    position: absolute;
    left: 280px;
    width: 640px;
    height: 366px;
    background: var(--white);
    overflow: hidden;
    box-shadow: 0 6px 18px rgba(0,0,0,.45);
  }
  .card--front { top: 60px; }
  .card--back  { top: 474px; }

  /* Brand lockup */
  .brand {
    display: flex;
    align-items: center;
    gap: 14px;
  }
  .brand__square {
    width: 34px; height: 34px;
    background: var(--grey);
  }
  .brand__name {
    color: var(--red);
    font-weight: 300;
    font-size: 40px;
    letter-spacing: 4px;
    line-height: 1;
  }
  .brand__tagline {
    color: var(--ink);
    font-weight: 700;
    font-size: 15px;
    letter-spacing: .5px;
    text-transform: uppercase;
    margin-top: 12px;
  }

  /* Front */
  .front__content {
    position: absolute; inset: 0;
    display: flex; flex-direction: column;
    align-items: center; justify-content: center;
  }
  .front__web {
    margin-top: 14px;
    font-size: 15px;
    color: var(--ink);
    letter-spacing: .4px;
  }

  /* Back */
  .back__logo {
    position: absolute;
    top: 34px; left: 0; right: 0;
    display: flex; flex-direction: column; align-items: center;
  }
  .back__logo .brand__name { font-size: 32px; }
  .back__logo .brand__square { width: 28px; height: 28px; }
  .back__logo .brand__tagline { font-size: 13px; margin-top: 8px; }

  .back__band {
    position: absolute; left: 0; right: 0; bottom: 0;
    height: 210px;
    background: var(--red);
    border-top: 4px solid var(--grey);
  }
  .back__notch { position: absolute; top: -4px; right: 64px; }

  .person {
    position: absolute; top: 20px; right: 28px;
    display: flex; gap: 12px; align-items: flex-start;
    text-align: right; color: var(--white);
  }
  .person__name { font-size: 26px; font-weight: 400; line-height: 1.1; }
  .person__role { font-size: 13px; }

  .address {
    position: absolute; top: 96px; right: 28px;
    display: flex; gap: 12px; align-items: flex-start;
    text-align: right; color: var(--white);
    font-size: 13px; line-height: 1.4;
  }

  .contacts {
    position: absolute; left: 28px; bottom: 18px;
    list-style: none;
    color: var(--white); font-size: 13.5px;
  }
  .contacts li {
    display: flex; align-items: center; gap: 12px;
    margin-top: 6px;
  }
  .icon {
    width: 26px; height: 26px; flex: none;
    border-radius: 50%;
    background: var(--white);
    display: flex; align-items: center; justify-content: center;
  }
  .icon svg { width: 14px; height: 14px; fill: var(--ink); }
</style>
</head>
<body>

<section class="card card--front" aria-label="Business card front">
  <div class="front__content">
    <div class="brand">
      <span class="brand__square"></span>
      <span class="brand__name">Velmorabelle</span>
    </div>
    <p class="brand__tagline">Private Label Solutions</p>
    <p class="front__web">www.velmorabelle.ch</p>
  </div>
</section>

<section class="card card--back" aria-label="Business card back">
  <div class="back__logo">
    <div class="brand">
      <span class="brand__square"></span>
      <span class="brand__name">Velmorabelle</span>
    </div>
    <p class="brand__tagline">Private Label Solutions</p>
  </div>

  <div class="back__band">
    <svg class="back__notch" width="28" height="16" viewBox="0 0 28 16" aria-hidden="true">
      <polygon points="0,0 28,0 14,16" fill="#6f6f6f"/>
    </svg>

    <div class="person">
      <div>
        <p class="person__name">Lucien Marchetaz</p>
        <p class="person__role">General Manager</p>
      </div>
      <span class="icon"><svg viewBox="0 0 16 16"><circle cx="8" cy="5" r="3.2"/><path d="M2 15c0-3.6 2.7-5.5 6-5.5s6 1.9 6 5.5z"/></svg></span>
    </div>

    <div class="address">
      <p>Chemin des Prés-Fleuris 14, 2000<br>Neuchâtel, Switzerland</p>
      <span class="icon"><svg viewBox="0 0 16 16"><path d="M8 1a5 5 0 0 0-5 5c0 3.8 5 9 5 9s5-5.2 5-9a5 5 0 0 0-5-5zm0 7a2 2 0 1 1 0-4 2 2 0 0 1 0 4z"/></svg></span>
    </div>

    <ul class="contacts">
      <li><span class="icon"><svg viewBox="0 0 16 16"><path d="M4.2 1.5l2 3-1.3 1.5a8 8 0 0 0 5.1 5.1l1.5-1.3 3 2-1.2 2.4C7 14 2 9 1.8 2.7z"/></svg></span>(+41 32 918 64 00)</li>
      <li><span class="icon"><svg viewBox="0 0 16 16"><path d="M1 3.5h14v9H1z M1.6 4l6.4 5 6.4-5" fill="none" stroke="#1c1c1c" stroke-width="1.5"/></svg></span>info@velmorabelle.ch</li>
      <li><span class="icon"><svg viewBox="0 0 16 16"><circle cx="8" cy="8" r="6.3" fill="none" stroke="#1c1c1c" stroke-width="1.4"/><path d="M1.7 8h12.6M8 1.7c-2.4 3.6-2.4 9 0 12.6M8 1.7c2.4 3.6 2.4 9 0 12.6" fill="none" stroke="#1c1c1c" stroke-width="1.2"/></svg></span>www.velmorabelle.ch</li>
    </ul>
  </div>
</section>

</body>
</html>
```